Business Card for Inovative Flexible Packaging Company

Create a business card that is both simple and stricking at the same time.
Preferably only one color (orange) or two colors (black and orange).
Information to print:
Torvalo, Lda
[T] 22 418 6093
[M] 91 326 7041
[F] 22 418 6135
[@] torvalo.ac@correiomx.com
SEDE & ARMAZÉM
Rua Das Figueiras do Monte, 312
Vilarelho
4785-832 Vilarelho - Vale Norte
PORTUGAL
Reason: A lot of the ideas are obvious. I want something different. Inovative. dare to do something eye catching with style.
Business Consumers. Packaging Designers.
Business

```html
<!DOCTYPE html>
<html lang="pt">
<head>
<meta charset="utf-8">
<title>Torvalo — Cartão de Visita</title>
<link rel="stylesheet" href="https://fonts.googleapis.com/css2?family=Noto+Serif:wght@400;700&display=swap">
<style>
  :root {
    --orange: #ff3d00;
    --orange-bright: #ff4a0a;
    --black: #111111;
    --white: #ffffff;
    --backdrop: #ededef;
    --ink: #1a1a1a;
  }
  * { margin: 0; padding: 0; box-sizing: border-box; }
  html, body {
    width: 1200px; height: 900px; overflow: hidden;
    background: var(--backdrop);
    font-family: "Noto Serif", Georgia, serif;
    color: var(--ink);
  }
  .canvas { position: relative; width: 1200px; height: 900px; }

  .card {
    position: absolute;
    width: 541px; height: 313px;
    box-shadow: 5px 6px 6px rgba(0,0,0,0.45);
    overflow: hidden;
  }
  .card-front {
    left: 52px; top: 176px;
    background: var(--orange);
    display: flex; align-items: center; justify-content: center;
  }
  .card-back {
    left: 632px; top: 176px;
    background: var(--white);
  }

  .brand-name {
    font-family: "Noto Serif", Georgia, serif;
    font-weight: 700;
    letter-spacing: -0.5px;
    line-height: 1;
    white-space: nowrap;
  }
  .card-front .brand-name { color: var(--black); font-size: 58px; }
  .card-back .brand-name {
    position: absolute; left: 22px; top: 22px;
    color: var(--orange); font-size: 38px;
  }

  .card-stripes { position: absolute; inset: 0; width: 100%; height: 100%; }

  .company-name {
    position: absolute; left: 43px; top: 132px;
    font-size: 19px; font-weight: 400;
  }
  .contact-list {
    position: absolute; left: 43px; top: 162px;
    list-style: none;
    font-size: 15.5px; line-height: 23px;
  }
  .contact-list li { display: flex; align-items: center; gap: 6px; white-space: nowrap; }
  .contact-icon { width: 13px; height: 13px; fill: var(--orange); flex: none; }

  .address {
    position: absolute; left: 275px; top: 156px;
    font-style: normal; font-size: 16px; line-height: 20.5px;
    white-space: nowrap;
  }

  .signature-brand {
    position: absolute; left: 930px; top: 786px;
    color: var(--orange-bright); font-size: 64px;
  }
</style>
</head>
<body>
<main class="canvas">

  <section class="card card-front" aria-label="Frente do cartão">
    <span class="brand-name">torvalo</span>
  </section>

  <section class="card card-back" aria-label="Verso do cartão">
    <svg class="card-stripes" viewBox="0 0 461 267" preserveAspectRatio="none" aria-hidden="true">
      <polygon points="0,2 318,2 309,7 0,7" fill="var(--black)"/>
      <polygon points="0,9 306,9 297,14 0,14" fill="var(--orange)"/>
      <polygon points="156,252 461,252 461,256 148,256" fill="var(--orange)"/>
      <polygon points="142,259 461,259 461,264 133,264" fill="var(--black)"/>
    </svg>

    <span class="brand-name">torvalo</span>

    <h1 class="company-name">Torvalo, Lda</h1>

    <ul class="contact-list">
      <li>
        <svg class="contact-icon" viewBox="0 0 24 24" aria-label="Telefone"><path d="M6.6 10.8a15 15 0 0 0 6.6 6.6l2.2-2.2c.3-.3.7-.4 1-.2 1.1.4 2.3.6 3.6.6.6 0 1 .4 1 1V20c0 .6-.4 1-1 1A17 17 0 0 1 3 4c0-.6.4-1 1-1h3.5c.6 0 1 .4 1 1 0 1.3.2 2.5.6 3.6.1.3 0 .7-.2 1z"/></svg>
        <span>22 418 6093</span>
      </li>
      <li>
        <svg class="contact-icon" viewBox="0 0 24 24" aria-label="Telemóvel"><path d="M7 1h10a2 2 0 0 1 2 2v18a2 2 0 0 1-2 2H7a2 2 0 0 1-2-2V3a2 2 0 0 1 2-2zm0 4v12h10V5zm5 14a1 1 0 1 0 0 2 1 1 0 0 0 0-2z"/></svg>
        <span>91 326 7041</span>
      </li>
      <li>
        <svg class="contact-icon" viewBox="0 0 24 24" aria-label="Fax"><path d="M7 2h10v6H7zM3 9h18a1 1 0 0 1 1 1v11a1 1 0 0 1-1 1H3a1 1 0 0 1-1-1V10a1 1 0 0 1 1-1zm3 4v2h3v-2zm5 0v2h3v-2zm5 0v2h3v-2zM6 17v2h3v-2zm5 0v2h3v-2z"/></svg>
        <span>22 418 6135</span>
      </li>
      <li>
        <svg class="contact-icon" viewBox="0 0 24 24" aria-label="Email"><path d="M2 5h20v14H2zm2 2v.5l8 5 8-5V7z"/></svg>
        <span>torvalo.ac@correiomx.com</span>
      </li>
    </ul>

    <address class="address">
      SEDE &amp; ARMAZÉM<br>
      Rua Das Figueiras do Monte, 312<br>
      Vilarelho<br>
      4785-832 Vilarelho - Vale Norte<br>
      PORTUGAL
    </address>
  </section>

  <span class="brand-name signature-brand">torvalo</span>

</main>
</body>
</html>
```